Harbor Business Cards

I need a business card designed with the following information.

Company Name: Harborvane Wealth Management
Name: BriAnne Dockery
Title: Executive Assistant
Cell: (281) 555-0173
Direct Line: (832) 555-0148
Email: brianne@harborwmx.com
Address: 20537 W. Marlowe PKWY Ste. B
Brackenford, TX 77390

I have attached the logo.
I would like it in navy blue and silver.
Thanks.

```html
<!DOCTYPE html>
<html lang="en">
<head>
<meta charset="utf-8">
<title>Harborvane Wealth Management – Business Card</title>
<link href="https://fonts.googleapis.com/css2?family=Work+Sans:wght@400;500;600&display=swap" rel="stylesheet">
<style>
  :root {
    --navy: #0f2141;
    --white: #ffffff;
    --ink-soft: #4a4f5a;
    --ink-mid: #3a3f4b;
    --backdrop: #dcdcdc;
  }
  * { box-sizing: border-box; margin: 0; padding: 0; }
  html, body { width: 1200px; height: 1000px; overflow: hidden; }
  body {
    background: var(--backdrop);
    font-family: "Work Sans", Arial, sans-serif;
    position: relative;
  }
  .card {
    position: absolute;
    left: 191px;
    width: 818px;
    height: 466px;
    overflow: hidden;
    box-shadow: 0 6px 14px rgba(0,0,0,0.18);
  }
  .card--front { top: 10px; background: var(--white); }
  .card--back { top: 523px; background: var(--navy); }

  /* brand block */
  .brand { position: absolute; text-align: center; }
  .brand__dot { display: block; margin: 0 auto; border-radius: 50%; }
  .brand__name, .brand__sub {
    display: block;
    font-weight: 500;
    text-transform: uppercase;
    white-space: nowrap;
  }
  .card--front .brand { left: 80px; width: 300px; top: 130px; }
  .card--front .brand__dot { width: 112px; height: 112px; background: var(--navy); margin-bottom: 20px; }
  .card--front .brand__name { color: var(--navy); font-size: 26px; letter-spacing: 0.3em; line-height: 34px; margin-right: -0.3em; }
  .card--front .brand__sub { color: var(--navy); font-size: 13px; letter-spacing: 0.26em; line-height: 16px; margin-top: 9px; margin-right: -0.26em; }

  .card--back .brand { left: 0; width: 818px; top: 90px; }
  .card--back .brand__dot { width: 170px; height: 170px; background: var(--white); margin-bottom: 32px; }
  .card--back .brand__name { color: var(--white); font-size: 38px; letter-spacing: 0.3em; line-height: 44px; margin-right: -0.3em; }
  .card--back .brand__sub { color: var(--white); font-size: 18px; letter-spacing: 0.24em; line-height: 22px; margin-top: 14px; margin-right: -0.24em; }

  .divider {
    position: absolute;
    left: 399px; top: 106px;
    width: 2px; height: 219px;
    background: var(--navy);
  }

  .contact { position: absolute; left: 431px; top: 104px; color: var(--ink-soft); }
  .contact__name {
    color: var(--navy);
    font-size: 29px;
    font-weight: 500;
    letter-spacing: 0.09em;
    text-transform: uppercase;
  }
  .contact__title {
    color: var(--ink-mid);
    font-size: 18px;
    font-weight: 500;
    letter-spacing: 0.04em;
    margin-top: 2px;
  }
  .contact__address { font-size: 18px; font-weight: 400; line-height: 21px; margin-top: 20px; }
  .contact__lines { list-style: none; margin-top: 22px; font-size: 18px; }
  .contact__lines li { display: flex; align-items: center; height: 25px; }
  .contact__lines svg { width: 13px; height: 13px; margin-right: 12px; fill: var(--navy); }

  .web-tab {
    position: absolute;
    right: 0; bottom: 0;
    width: 396px; height: 34px;
    background: var(--navy);
    clip-path: polygon(36px 0, 100% 0, 100% 100%, 0 100%);
    color: var(--white);
    font-size: 18px;
    display: flex; align-items: center;
    padding-left: 106px;
  }
  .web-tab b, .web-back b { font-weight: 600; }
  .web-back {
    position: absolute;
    left: 0; width: 818px; top: 423px;
    text-align: center;
    color: var(--white);
    font-size: 18px;
  }
</style>
</head>
<body>
  <section class="card card--front">
    <div class="brand">
      <span class="brand__dot"></span>
      <span class="brand__name">Harborvane</span>
      <span class="brand__sub">Wealth Management</span>
    </div>
    <div class="divider"></div>
    <div class="contact">
      <h1 class="contact__name">BriAnne Dockery</h1>
      <p class="contact__title">Executive Assistant</p>
      <p class="contact__address">20537 W. Marlowe Pkwy Ste.<br>B Brackenford, Tx 77390</p>
      <ul class="contact__lines">
        <li><svg viewBox="0 0 16 16"><path d="M4 1l2.5 3-1.5 2c1 2 3 4 5 5l2-1.5 3 2.5-1.5 2.5C7 15 1 9 1.5 3.5z"/></svg>(281) 555-0173</li>
        <li><svg viewBox="0 0 16 16"><path d="M4 0h8a1 1 0 0 1 1 1v14a1 1 0 0 1-1 1H4a1 1 0 0 1-1-1V1a1 1 0 0 1 1-1zm1 2v10h6V2zm3 11a1 1 0 1 0 0 2 1 1 0 0 0 0-2z"/></svg>(832) 555-0148</li>
        <li><svg viewBox="0 0 16 16"><path d="M1 3h14v10H1zm1.5 1.5v.4L8 8.6l5.5-3.7v-.4zm0 2.2v4.8h11V6.7L8 10.4z"/></svg>brianne@harborwmx.com</li>
      </ul>
    </div>
    <div class="web-tab">www.<b>BriAnneDockery</b>.com</div>
  </section>

  <section class="card card--back">
    <div class="brand">
      <span class="brand__dot"></span>
      <span class="brand__name">Harborvane</span>
      <span class="brand__sub">Wealth Management</span>
    </div>
    <p class="web-back">www.<b>harborvanewealthx</b>.com</p>
  </section>
</body>
</html>
```